Redesign our website!

Tandel’s current web (http://tandelwear.example) site was implemented in 2012 and needs to be brought up to date with look and feel of our new packaging and logo. The layout of Tandel’s website is fairly consistent from page to page; utilizing only two very similar “templates” or “themes.”

Project Description:
Tandel is seeking a designer to gain inspiration from our new packaging, design and recent print ad and create a new look for our website (http://tandelwear.example); focusing on the wallpaper, background, navigation bars/buttons, header and footer. Additionally, Tandel needs a new “style” for the images used in the slideshow on the homepage as well as the banner images on the product category/subcategory pages.

It is important that element height/width and positioning of elements (such as the "feature" boxes on the homepage, navigation bar, and banner images) within the pages are not changed in the new design. In other words, this project is solely focused on the overall design, not the specific layouts of each page.

Attached are:
* a zip file of JPEG examples of our new packaging;
* a pdf copy of a print ad we recently used for an industry tradeshow;
* a zip file with 2 JPEGS of images used in our booth at the above mentioned tradeshow;
* a JPEG of our new logo;
* a JPEG of the Background used on our new packing.

The model images that can be used in the mock-up of the new homepage slideshow but please do not feel as though you need to use the models in your banner mock-up. If you use your own models (stock images are OK,) please try to incorporate our products on the models.This will help us get a realistic sense of your direction.
Updates

I am very encouraged by the examples I am seeing. Thank you to those who have contributed and to those still working on it, please do! This is by no means a done deal with any one design.

One tip to those who have already contributed and those still to do so: we are looking for a new color scheme. Please do not use the brown/green you see on the current site.  Thank you.

Requirements
Must have
• Remove "Vines" from the background"
Change the header to less look "yoga"ish
1 "sample" image for the homepage slideshow
1 "sample image" for a category banner (i.e. the banner on http://tandelwear.example/wristos/)

```html
<!DOCTYPE html>
<html lang="en">
<head>
<meta charset="utf-8">
<title>Tandel — Find Your Rhythm</title>
<link href="https://fonts.googleapis.com/css2?family=Comfortaa:wght@300;400&family=Open+Sans:ital,wght@0,400;0,600;1,400&display=swap" rel="stylesheet">
<style>
:root{
  --orange:#f04a12;
  --ink:#1a1a1a;
  --black:#000;
  --white:#fff;
  --grey-text:#7a7a7a;
  --footer:#333333;
  --footer-line:#4a4a4a;
  --footer-text:#f2f2f2;
  --muted:#8a8a8a;
  --search:#4a4a4a;
}
*{margin:0;padding:0;box-sizing:border-box}
html,body{width:1200px;height:1166px;overflow:hidden;background:var(--white)}
body{position:relative;font-family:"Open Sans",Arial,sans-serif;color:var(--ink)}
.abs{position:absolute}

/* header */
.brand{left:186px;top:10px;font-family:"Comfortaa",sans-serif;font-size:40px;color:#555;letter-spacing:-1px}
.top-contact{left:786px;top:14px;font-size:12px;display:flex;gap:10px;align-items:center;white-space:nowrap}
.top-contact .phone{color:var(--orange);font-size:13px;display:flex;align-items:center;gap:2px}
.social-mini{top:42px;width:20px;height:20px;border-radius:50%;background:#555}
.search{left:882px;top:42px;width:130px;height:21px;background:var(--search);color:#bbb;font-size:10px;padding:4px 8px}
.search svg{position:absolute;right:6px;top:4px}

/* nav */
.nav{left:0;top:77px;width:1200px;height:44px;background:var(--black)}
.nav-list{position:absolute;left:189px;top:0;width:821px;height:44px;display:flex;justify-content:space-between;align-items:center}
.nav-list a{color:var(--white);text-decoration:none;font-family:"Comfortaa",sans-serif;font-size:15px;white-space:nowrap}

/* hero */
.hero{left:0;top:121px;width:1200px;height:359px;background:linear-gradient(90deg,#cdbfc1 0%,#d9cfd1 30%,#dcd2d4 60%,#e3dadc 100%)}
.hero-title{left:546px;top:196px;font-family:"Comfortaa",sans-serif;font-size:46px;color:var(--ink);letter-spacing:-1px;white-space:nowrap}
.hero-copy{left:547px;top:265px;font-family:Arial,sans-serif;font-size:15px;line-height:19px;color:#111;white-space:nowrap}
.btn{background:var(--orange);color:var(--white);font-family:"Comfortaa",sans-serif;display:flex;align-items:center;white-space:nowrap}
.hero-btn{left:546px;top:320px;width:228px;height:34px;font-size:13px;padding-left:29px;clip-path:polygon(0 0,91% 0,100% 50%,91% 100%,0 100%)}
.slide-arrow{top:279px;width:39px;height:39px;border-radius:50%;background:rgba(255,255,255,.3);display:flex;align-items:center;justify-content:center}
.dot{top:456px;width:9px;height:9px;border-radius:50%;background:rgba(255,255,255,.75)}

/* features */
.section-title{font-family:"Comfortaa",sans-serif;font-size:20px;color:var(--ink);white-space:nowrap}
.lead{font-size:12.4px;line-height:14px;color:var(--grey-text);white-space:nowrap}
.tag-btn{left:652px;top:539px;width:122px;height:18px;font-family:"Open Sans",sans-serif;font-size:8.5px;padding-left:8px;clip-path:polygon(0 0,92% 0,100% 50%,92% 100%,0 100%)}
.tile{top:617px;width:185px;height:161px}
.tile .cap{position:absolute;left:0;bottom:0;width:100%;height:34px;background:rgba(0,0,0,.72);color:var(--white);font-size:13px;display:flex;align-items:center;justify-content:center;letter-spacing:-.2px;white-space:nowrap}
.showcase{left:800px;top:616px;width:194px;height:162px;border:2px solid #e6e6e6;background:var(--white)}
.pack{position:absolute;top:11px;width:67px;height:144px}
.round-btn{top:771px;width:18px;height:18px;border-radius:50%;background:var(--orange);display:flex;align-items:center;justify-content:center}

/* footer */
.footer{left:0;top:832px;width:1200px;height:334px;background:var(--footer);color:var(--footer-text)}
.footer h3{position:absolute;top:40px;font-family:"Comfortaa",sans-serif;font-weight:400;font-size:17px;white-space:nowrap}
.links{position:absolute;top:76px;list-style:none}
.links li{height:27px;border-bottom:1px solid var(--footer-line);font-size:11.2px;display:flex;align-items:center;gap:5px;padding-left:4px;white-space:nowrap}
.links li:last-child{border-bottom:none}
.links li::before{content:"⇢";font-size:9px;color:#ccc}
.news{position:absolute;left:491px;width:260px;font-size:11px;line-height:13px;white-space:nowrap}
.news .title{color:var(--orange)}
.news .date{color:var(--muted);font-style:italic;margin-left:8px}
.share{position:absolute;top:82px;width:42px;height:42px;border-radius:50%;background:var(--white)}
.contact-line{position:absolute;left:798px;font-size:14.4px;display:flex;align-items:center;gap:8px;white-space:nowrap}
.foot-btn{position:absolute;left:798px;top:196px;width:206px;height:34px;font-size:13px;justify-content:center;clip-path:polygon(0 0,100% 0,97% 50%,100% 100%,0 100%,3% 50%)}
.foot-brand{position:absolute;left:192px;top:262px;font-family:"Comfortaa",sans-serif;font-size:22px;color:#666}
.copyright{position:absolute;left:281px;top:266px;font-size:10px;color:#aaa;white-space:nowrap}
</style>
</head>
<body>

<header>
  <div class="abs brand">Tandel</div>
  <div class="abs top-contact">
    <span class="phone"><svg width="9" height="11" viewBox="0 0 9 11"><path d="M2 0l2 3-1 1c.5 1.5 1.5 2.6 3 3.3l1-1 2 2-1.5 2C3.5 10 0 6 .3 1.5z" fill="#f04a12"/></svg>555-010-2866</span>
    <span>My Account</span>
    <span style="margin-left:8px">Cart : 01</span>
  </div>
  <span class="abs social-mini" style="left:785px"></span>
  <span class="abs social-mini" style="left:815px"></span>
  <span class="abs social-mini" style="left:844px"></span>
  <div class="abs search">Search
    <svg width="12" height="12" viewBox="0 0 12 12"><circle cx="5" cy="5" r="3.8" fill="none" stroke="#ccc" stroke-width="1.5"/><path d="M8 8l3 3" stroke="#ccc" stroke-width="1.6"/></svg>
  </div>
</header>

<nav class="abs nav">
  <div class="nav-list">
    <a>Home</a>
    <a>About</a>
    <a>Wristos Wrist Wallets</a>
    <a>Earhugs Ear Warmers</a>
    <a>Apparel</a>
    <a>Accessories</a>
    <a>Eco Products</a>
  </div>
</nav>

<section class="abs hero" role="img" aria-label="Slideshow photo of a woman in a patterned headband and black top, wearing earphones and a wrist wallet">
</section>
<h1 class="abs hero-title" style="font-weight:400">find your rhythm</h1>
<p class="abs hero-copy">ermentum dolor non augue pretium egestas donec est<br>sem eros, tincidunt at congue ut, posuere sit amet</p>
<div class="abs btn hero-btn">GET IN THOUCH WITH US</div>
<div class="abs slide-arrow" style="left:149px"><svg width="10" height="14" viewBox="0 0 10 14"><path d="M8 1L2 7l6 6" fill="none" stroke="#fff" stroke-width="2.5"/></svg></div>
<div class="abs slide-arrow" style="left:1015px"><svg width="10" height="14" viewBox="0 0 10 14"><path d="M2 1l6 6-6 6" fill="none" stroke="#fff" stroke-width="2.5"/></svg></div>
<span class="abs dot" style="left:575px"></span>
<span class="abs dot" style="left:589px"></span>
<span class="abs dot" style="left:603px"></span>
<span class="abs dot" style="left:617px"></span>

<main>
  <h2 class="abs section-title" style="left:246px;top:536px;font-weight:400">Our Features Products, H2 Heading</h2>
  <div class="abs btn tag-btn">VIEW OUR ALL FEATURS</div>
  <p class="abs lead" style="left:208px;top:570px">Lorem ipsum dolor sit amet, consectetur adipisicing elit, sed do eiusmod tempor incididunt<br>ut labore et dolore magna aliqua. Ut enim ad minim veniam, quis nostrud exercitation</p>

  <div class="abs tile" style="left:208px;background:linear-gradient(135deg,#c25a3a,#5d7a4a 45%,#6a5a4a)" role="img" aria-label="Photo of a green leather wrist wallet on an arm">
    <div class="cap">You Can Take It with You</div>
  </div>
  <div class="abs tile" style="left:400px;background:linear-gradient(180deg,#b8bcc2 0%,#8f969b 45%,#5a6a44 100%)" role="img" aria-label="Photo of two runners by a lake">
    <div class="cap">Wristos Wrist Wallets</div>
  </div>
  <div class="abs tile" style="left:592px;background:linear-gradient(135deg,#5e6240,#726f52 50%,#4b4a36)" role="img" aria-label="Photo of a braided leather cuff on a wrist">
    <div class="cap">H3 Lorem Ipsum Head</div>
  </div>

  <h2 class="abs section-title" style="left:838px;top:536px;font-weight:400">Look at THAT!</h2>
  <p class="abs lead" style="left:799px;top:570px">Lorem ipsum dolor sit amet, sed<br>do eiusmod tempor incididunt</p>
  <div class="abs showcase">
    <div class="pack" style="left:22px;background:linear-gradient(180deg,#3a3f48,#2c323b 70%,#3aa84a 92%)" role="img" aria-label="Wrist wallet packaging, classic edition"></div>
    <div class="pack" style="left:96px;background:linear-gradient(180deg,#3a3f48,#2c323b 70%,#1fa3d8 92%)" role="img" aria-label="Wrist wallet packaging, two pocket edition"></div>
  </div>
  <div class="abs round-btn" style="left:873px"><svg width="6" height="8" viewBox="0 0 6 8"><path d="M5 1L2 4l3 3" fill="none" stroke="#fff" stroke-width="1.8"/></svg></div>
  <div class="abs round-btn" style="left:897px"><svg width="6" height="8" viewBox="0 0 6 8"><path d="M1 1l3 3-3 3" fill="none" stroke="#fff" stroke-width="1.8"/></svg></div>
</main>

<footer class="abs footer">
  <h3 style="left:187px">Tandel Information</h3>
  <h3 style="left:487px">Latest News</h3>
  <h3 style="left:798px">Our Social Share</h3>

  <ul class="links" style="left:187px;width:85px">
    <li>Home</li><li>About</li><li>Services</li><li>Press/Media</li><li>Contact</li><li>Blog</li>
  </ul>
  <ul class="links" style="left:293px;width:129px">
    <li>Advocates &amp; Affiliates..</li><li>Back Story</li><li>News</li><li>Join Our Mailing List</li><li>Returns/Exchanges</li><li>FAQs</li>
  </ul>

  <div class="news" style="top:78px"><span class="title">News Heading Boold</span><span class="date">03 SEP 2013</span><br>Lorem ipsum dolor sit amet, adipisicing elit,<br>sed do eiusmod tempor incididunt ut labore</div>
  <div class="news" style="top:125px"><span class="title">News Heading Boold</span><span class="date">03 SEP 2013</span><br>Lorem ipsum dolor sit amet, adipisicing elit,<br>sed do eiusmod tempor incididunt ut labore</div>
  <div class="news" style="top:179px"><span class="title">News Heading Boold</span><span class="date">03 SEP 2013</span><br>Lorem ipsum dolor sit amet, adipisicing elit,<br>sed do eiusmod tempor incididunt ut labore</div>

  <span class="share" style="left:798px"></span>
  <span class="share" style="left:852px"></span>
  <span class="share" style="left:905px"></span>
  <span class="share" style="left:958px"></span>

  <div class="contact-line" style="top:138px"><svg width="12" height="14" viewBox="0 0 9 11"><path d="M2 0l2 3-1 1c.5 1.5 1.5 2.6 3 3.3l1-1 2 2-1.5 2C3.5 10 0 6 .3 1.5z" fill="#fff"/></svg><span>555-010-2866 <span style="color:#29a8e0">F</span> 555-010-2867</span></div>
  <div class="contact-line" style="top:159px"><svg width="14" height="10" viewBox="0 0 14 10"><rect x=".5" y=".5" width="13" height="9" fill="none" stroke="#fff"/><path d="M.5 .5L7 6l6.5-5.5" fill="none" stroke="#fff"/></svg><span>sales@tandelwear.example</span></div>
  <div class="btn foot-btn">GET IN THOUCH WITH US</div>

  <div class="foot-brand">Tandel</div>
  <div class="copyright">All right reserved with copyright © 2013 www.tandelwear.example - Terms</div>
</footer>

</body>
</html>
```